Company or website name
- Fernhollow Plank Co. Newsletter
- We sell butcher blocks, butcher block counters, butcher block tables, butcher block cutting boards, and other gourmet kitchen items.

```html
<!DOCTYPE html>
<html lang="en">
<head>
<meta charset="utf-8">
<title>Fernhollow Plank Co. News</title>
<link href="https://fonts.googleapis.com/css2?family=Tinos:ital,wght@0,400;0,700;1,700&family=Arimo:ital,wght@0,400;0,700;1,400&family=Parisienne&display=swap" rel="stylesheet">
<style>
:root{
  --page:#ffffff;
  --title-grey:#808080;
  --news-rust:#a0380f;
  --band-red:#800000;
  --band-rule:#2f4f5a;
  --panel-red:#962311;
  --body-grey:#4a4a4a;
  --quote-grey:#5a5a5a;
  --frame-grey:#d6d6d6;
  --wood-dark:#6b4028;
  --wood-mid:#8a5a36;
  --table-light:#d9b88a;
  --table-mid:#c49968;
}
*{margin:0;padding:0;box-sizing:border-box}
html,body{width:927px;height:1200px;overflow:hidden;background:var(--page)}
.page{position:relative;width:927px;height:1200px}
.masthead-thumb{position:absolute;left:44px;top:51px;width:213px;height:180px;border:1px solid var(--frame-grey);background:#fff;padding:28px 14px}
.masthead-thumb .fill{width:100%;height:100%;background:linear-gradient(180deg,var(--wood-mid),var(--wood-dark))}
.brand-title{position:absolute;left:284px;top:86px;font-family:"Tinos",serif;font-size:62px;color:var(--title-grey);white-space:nowrap;line-height:1}
.issue-info{position:absolute;left:426px;top:194px;font-family:"Tinos",serif;font-size:14px;line-height:16px;color:#111}
.news-word{position:absolute;left:668px;top:150px;font-family:"Parisienne",cursive;font-size:82px;color:var(--news-rust);line-height:1}
.tagline-band{position:absolute;left:15px;top:264px;width:895px;height:31px;background:var(--band-red);border-bottom:2px solid var(--band-rule);border-right:2px solid var(--band-rule);color:#fff;font-family:"Tinos",serif;font-size:24px;text-align:center;line-height:29px}
.headline{position:absolute;left:29px;top:337px;font-family:"Arimo",sans-serif;font-size:19px;color:#111}
.feature-photo{position:absolute;left:57px;top:376px;width:453px;height:355px;border:1px solid var(--frame-grey);background:#fff;padding:20px 30px}
.feature-photo .fill{width:100%;height:100%;background:linear-gradient(180deg,var(--table-mid) 0%,var(--table-light) 45%,#efe2cc 100%)}
.caption{position:absolute;left:44px;top:746px;font-family:"Tinos",serif;font-weight:700;font-size:14.5px;color:#111}
.column{position:absolute;font-family:"Arimo",sans-serif;font-size:17px;line-height:21px;letter-spacing:.35px;color:var(--body-grey);text-align:justify}
.col-left{left:29px;top:803px;width:241px}
.col-left p{text-indent:44px}
.col-right{left:294px;top:789px;width:231px}
.sidebar{position:absolute;left:567px;top:334px;width:311px;height:793px;background:var(--panel-red);box-shadow:4px 4px 0 #222}
.sidebar-head{position:absolute;left:14px;top:28px;width:284px;height:86px;background:#fff;border:1px solid #7a1a0c;font-family:"Tinos",serif;font-weight:700;font-style:italic;font-size:25px;line-height:31px;text-align:center;padding-top:11px;color:#111}
.quotes{position:absolute;left:28px;top:127px;width:256px;height:651px;background:#fff;border:1px solid #7a1a0c;padding:30px 16px 0 12px;font-family:"Arimo",sans-serif;font-size:16px;line-height:21px;letter-spacing:.3px;color:var(--quote-grey)}
.quote-text{font-weight:700}
.quote-author{font-style:italic}
.gap{height:21px}
</style>
</head>
<body>
<div class="page">
  <div class="masthead-thumb" role="img" aria-label="Walnut butcher block countertop"><div class="fill"></div></div>
  <div class="brand-title">Fernhollow Plank Co.</div>
  <div class="issue-info">Volume 12, Issue 19<br>June 10, 2010</div>
  <div class="news-word">News</div>

  <div class="tagline-band">The finest selection of Butcher Blocks.</div>

  <div class="headline">New Product line unveiled at Grand Opening</div>
  <div class="feature-photo" role="img" aria-label="Maple butcher block kitchen table with drawers, a bowl of apples and a stock pot on the lower shelf"><div class="fill"></div></div>
  <div class="caption">The New Butcher Block Table, every cook’s best friend.</div>

  <div class="column col-left">
    <p>Our gorgeous butcher block kitchen islands come in a wide array of sizes and styles to suit any setting. Featuring popular add-ons such as rolling caster wheels, knife racks, towel bars, outlet strips, and more, these butcher block kitchen islands offer everything you need to increase your kitchen storage and work space with style and convenience. We also feature butcher block kitchen island tables made-to-order in the USA to the highest</p>
  </div>
  <div class="column col-right">
    <p>standards of craftsmanship with only the finest solid hardwoods. Use the links below to browse our full collection of butcher block kitchen islands, or use the search box above to narrow your search. Enjoy!</p>
    <p>standards of craftsmanship with only the finest solid hardwoods. Use the links below to browse our full collection of butcher block kitchen islands, or use the search box above to narrow your search. Enjoy!</p>
  </div>

  <aside class="sidebar">
    <div class="sidebar-head">What our Customers<br>are saying</div>
    <div class="quotes">
      <div class="quote-text">"What a great product! It fits perfectly on the cabinet we ordered it for and my wife couldn't be happier with the look and construction</div>
      <div class="quote-author">Martin R.Brownsville, TX</div>
      <div class="quote-text">"Thank you and keep up the good work!"</div>
      <div class="quote-author">Dennis K.<br>East Syracuse, NY</div>
      <div class="gap"></div>
      <div class="quote-text">"I would use this merchant again, I bought a butcher block counter top and it is beautiful, and a great price. Customer service was excellent!!!"</div>
      <div class="quote-author">Lena P.<br>Brockton, MA</div>
      <div class="gap"></div>
      <div class="quote-text">"I was very pleased with the service from the Fernhollow Plank Co use this company again in the future. Thank you!"</div>
      <div class="quote-author">Rachel T.Henderson, NV</div>
    </div>
  </aside>
</div>
</body>
</html>
```